Barrowdale Power Loft Chronic Pain Flyer

Double sided DL flyer required to promote a strength training studio to sufferers of chronic pain. Flyer will be displayed in osteopathy, chiropractic and massage clinics. Flyer should be clean, professional and appeal to an older (40+) demographic.

Target Market(s)

Chronic pain sufferers. Age 40+

Industry/Entity Type

Health And Wellness

Colors

Designer to choose colors to be used in the design.

Requirements
Must have
• See attached files for text copy and logo. Image(s) of people strength training with a coach or personal trainer, as well as images depicting pain in common parts of the body (such as those pictured in the supplied mock up)
• website address: barrowdalepowerloft.com.au
• phone number : 0452 918 064
• Street address: 4/83 Kinross Hill Rd, Barrowdale
Nice to have
• Images such as in the attached files.

```html
<!DOCTYPE html>
<html lang="en">
<head>
<meta charset="utf-8">
<title>Barrowdale Power Loft – Chronic Pain Flyer</title>
<link rel="stylesheet" href="https://fonts.googleapis.com/css2?family=Anton&family=Open+Sans:wght@400;600;700;800&display=swap">
<style>
  :root{
    --page:#e9e6e1;
    --header:#3f3d3d;
    --paper:#f6f6f6;
    --red:#d9332b;
    --red-dark:#8e1a15;
    --ink:#1e1e1e;
    --grey-light:#f2f2f2;
    --grey-mid:#b9b9b9;
    --white:#ffffff;
  }
  *{box-sizing:border-box;margin:0;padding:0}
  html,body{width:1200px;height:844px;overflow:hidden;background:var(--page)}
  .canvas{position:relative;width:1200px;height:844px}
  .flyer{
    position:absolute;top:42px;width:360px;height:760px;
    background:var(--paper);overflow:hidden;
    box-shadow:0 6px 18px rgba(0,0,0,.18);
    font-family:"Open Sans",Arial,sans-serif;color:var(--ink);
  }
  .flyer--front{left:200px}
  .flyer--back{left:640px}

  .brand-band{
    height:160px;background:var(--header);
    display:flex;align-items:center;justify-content:center;gap:10px;
  }
  .brand-band__dot{width:14px;height:14px;border-radius:50%;background:var(--red)}
  .brand-band__name{
    font-family:"Open Sans",Arial,sans-serif;font-weight:800;
    font-size:23px;color:var(--white);letter-spacing:.5px;text-transform:uppercase;
  }

  .headline{
    font-family:"Anton",Impact,sans-serif;color:var(--red);
    text-align:center;line-height:.95;text-transform:uppercase;
    text-shadow:2px 2px 0 var(--red-dark);
  }
  .headline__top{display:block;font-size:33px;letter-spacing:1px}
  .headline__main{display:block;font-size:62px;letter-spacing:1px}
  .flyer--front .headline{margin-top:22px}
  .flyer--back .headline{margin-top:26px}

  .tagline{font-weight:700;font-size:15px;text-align:center;margin-top:6px}
  .copy{font-size:12.5px;line-height:1.32;padding:0 24px}
  .copy--intro{margin-top:10px;text-align:center}
  .copy--side{width:190px;margin-top:12px}

  .photo{position:absolute}
  .photo--knee{
    right:0;top:395px;width:170px;height:215px;
    background:radial-gradient(circle at 40% 55%,#e46a63 0,#c9a5a3 22%,#cfcfcf 45%,#9a9a9a 100%);
  }
  .photo--back{
    left:40px;top:395px;width:280px;height:115px;
    background:radial-gradient(ellipse at 50% 60%,#e05a52 0,#d4aaa7 28%,#d6d6d6 55%,#f0f0f0 100%);
  }
  .photo--shoulder{
    left:70px;top:520px;width:220px;height:100px;
    background:radial-gradient(ellipse at 50% 40%,#e05a52 0,#cfa3a0 25%,#bdbdbd 55%,#e8e8e8 100%);
  }

  .contact-band{position:absolute;left:0;bottom:0;width:360px;height:175px}
  .contact-band__shape{position:absolute;inset:0}
  .contact-band__text{
    position:absolute;left:0;right:0;top:48px;text-align:center;
  }
  .contact-band__phone{font-weight:800;font-size:22px;letter-spacing:.5px}
  .contact-band__line{font-size:15.5px;line-height:1.3}
</style>
</head>
<body>
<main class="canvas">

  <!-- Front side -->
  <article class="flyer flyer--front">
    <header class="brand-band">
      <span class="brand-band__dot"></span>
      <span class="brand-band__name">Barrowdale Power Loft</span>
    </header>
    <h1 class="headline">
      <span class="headline__top">Health Through</span>
      <span class="headline__main">Strength</span>
    </h1>
    <p class="tagline">You don't have to live in pain.</p>
    <p class="copy copy--intro">Strength training has been shown to improve many chronic pain conditions and is now being routinely recommended by medical and health professionals.</p>
    <p class="copy copy--side">Our private studio provides high quality strength training by expert strength coaches. We've helped countless people improve or eliminate chronic pain, contact us today and find out how we can help you.</p>
    <div class="photo photo--knee" role="img" aria-label="Black and white photo of hands holding a knee with a red glow marking pain"></div>
    <footer class="contact-band">
      <svg class="contact-band__shape" viewBox="0 0 360 175" preserveAspectRatio="none" aria-hidden="true">
        <defs>
          <linearGradient id="band-front" x1="0" y1="0" x2="0" y2="1">
            <stop offset="0" stop-color="#ffffff"/>
            <stop offset="1" stop-color="#a9a9a9"/>
          </linearGradient>
        </defs>
        <path d="M0 34 Q180 0 360 34 L360 175 L0 175Z" fill="url(#band-front)"/>
        <path d="M0 34 Q180 0 360 34" fill="none" stroke="#d9332b" stroke-width="4"/>
      </svg>
      <div class="contact-band__text">
        <p class="contact-band__phone">0452 918 064</p>
        <p class="contact-band__line">barrowdalepowerloft.com.au</p>
        <p class="contact-band__line">4/83 Kinross Hill Rd, Barrowdale</p>
      </div>
    </footer>
  </article>

  <!-- Back side -->
  <article class="flyer flyer--back">
    <header class="brand-band">
      <span class="brand-band__dot"></span>
      <span class="brand-band__name">Barrowdale Power Loft</span>
    </header>
    <h2 class="headline">
      <span class="headline__top">Health Through</span>
      <span class="headline__main">Strength</span>
    </h2>
    <div class="photo photo--back" role="img" aria-label="Black and white photo of hands pressing a lower back with a red glow marking pain"></div>
    <div class="photo photo--shoulder" role="img" aria-label="Black and white photo of a person holding a sore shoulder with a red glow marking pain"></div>
    <footer class="contact-band">
      <svg class="contact-band__shape" viewBox="0 0 360 175" preserveAspectRatio="none" aria-hidden="true">
        <defs>
          <linearGradient id="band-back" x1="0" y1="0" x2="0" y2="1">
            <stop offset="0" stop-color="#ffffff"/>
            <stop offset="1" stop-color="#a9a9a9"/>
          </linearGradient>
        </defs>
        <path d="M0 34 Q180 0 360 34 L360 175 L0 175Z" fill="url(#band-back)"/>
        <path d="M0 34 Q180 0 360 34" fill="none" stroke="#d9332b" stroke-width="4"/>
      </svg>
      <div class="contact-band__text">
        <p class="contact-band__phone">0452 918 064</p>
        <p class="contact-band__line">barrowdalepowerloft.com.au</p>
        <p class="contact-band__line">4/83 Kinross Hill Rd, Barrowdale</p>
      </div>
    </footer>
  </article>

</main>
</body>
</html>
```